Automotive parts Package (box) design

We are developing a new packaging concept for our automotive service and suspension parts line. I will share 2–3 sample designs—some from other brands and some AI‑generated—and we need a designer to create a unified, original design direction based on these references.

We already have an established brand name, KEM, along with a logo. The logo may be updated or redesigned, but the brand name KEM must remain.

- The project includes creating the full packaging design for our product boxes, developing or refining the logo if needed.

-Then, after choosing the design, we will apply the same design to 8 boxes with small customisation for each box to match the product.

- The box die-lines will be provided by us.

Attached are a few sample designs. We need you to develop three or more new designs in a similar style. If you have additional creative concepts beyond these references, you are welcome to include them. The only fixed requirement is that the brand name KEM must remain unchanged in all proposed designs.

Box files such as PNG, PDF (ready-to-print file) and Ai (Editable/ Source file) and fonts with 3D mockup images at the end of the project must be given to us.

Target Market(s)

Car spare parts shops

Industry/Entity Type

Auto Parts

Requirements
Must have
• Our brand name KEM
Nice to have
• Package similar to big auto parts suppliers such as PLW, VARNE

```html
<!DOCTYPE html>
<html lang="en">
<head>
<meta charset="utf-8">
<title>KEM Service Parts – Box Front Panel</title>
<link rel="stylesheet" href="https://fonts.googleapis.com/css2?family=Anton&family=Montserrat:wght@600;800&display=swap">
<style>
  :root {
    --canvas-bg: #e2e2e2;
    --panel-black: #0b0b0b;
    --panel-white: #efefef;
    --brand-red: #c8141b;
    --deep-red: #5a0006;
    --bright-red: #e8221e;
    --silver-light: #ffffff;
    --silver-mid: #c9c9c9;
    --ink-dark: #1a1a1a;
  }
  html, body {
    margin: 0;
    padding: 0;
    width: 718px;
    height: 1200px;
    overflow: hidden;
    background: var(--canvas-bg);
  }
  .box-front {
    position: absolute;
    left: 29px;
    top: 416px;
    width: 660px;
    height: 367px;
    box-shadow: 0 18px 30px rgba(0,0,0,0.28);
  }
  .box-front svg { display: block; width: 100%; height: 100%; }
  .headline {
    font-family: "Anton", "Impact", sans-serif;
    font-size: 168px;
    letter-spacing: -2px;
  }
  .brand-name {
    font-family: "Montserrat", sans-serif;
    font-weight: 800;
    font-size: 84px;
    fill: var(--brand-red);
  }
  .brand-tagline {
    font-family: "Montserrat", sans-serif;
    font-weight: 600;
    font-size: 15px;
    letter-spacing: 3px;
    fill: var(--ink-dark);
  }
  .warranty-label {
    font-family: "Montserrat", sans-serif;
    font-weight: 800;
    font-size: 16px;
    letter-spacing: 1px;
  }
  .warranty-number {
    font-family: "Montserrat", sans-serif;
    font-weight: 800;
    font-size: 46px;
    fill: #ffffff;
  }
</style>
</head>
<body>
  <div class="box-front">
    <svg viewBox="0 0 1152 640" xmlns="http://www.w3.org/2000/svg">
      <defs>
        <linearGradient id="redBand" x1="0" y1="0" x2="1" y2="0">
          <stop offset="0" stop-color="var(--deep-red)"/>
          <stop offset="0.55" stop-color="#a8070d"/>
          <stop offset="1" stop-color="var(--brand-red)"/>
        </linearGradient>
        <linearGradient id="silverText" x1="0" y1="0" x2="0" y2="1">
          <stop offset="0" stop-color="var(--silver-light)"/>
          <stop offset="0.55" stop-color="#f2f2f2"/>
          <stop offset="1" stop-color="var(--silver-mid)"/>
        </linearGradient>
        <linearGradient id="silverLine" x1="0" y1="0" x2="1" y2="0">
          <stop offset="0" stop-color="#9a9a9a"/>
          <stop offset="0.5" stop-color="#ffffff"/>
          <stop offset="1" stop-color="#8c8c8c"/>
        </linearGradient>
        <linearGradient id="productArea" x1="0" y1="0" x2="0" y2="1">
          <stop offset="0" stop-color="#d6d6d6"/>
          <stop offset="1" stop-color="#8f8f8f"/>
        </linearGradient>
        <pattern id="redDashes" width="20" height="14" patternUnits="userSpaceOnUse" patternTransform="skewX(-30)">
          <rect x="0" y="0" width="10" height="14" fill="var(--bright-red)"/>
        </pattern>
      </defs>

      <!-- base -->
      <rect class="panel-base" width="1152" height="640" fill="var(--panel-black)"/>

      <!-- white diagonal brand panel -->
      <polygon class="brand-panel" points="650,0 1045,0 1152,310 1152,640 870,640" fill="var(--panel-white)"/>

      <!-- silver rule -->
      <rect class="silver-rule" x="0" y="82" width="562" height="8" fill="url(#silverLine)"/>

      <!-- red headline band -->
      <polygon class="headline-band" points="0,94 662,94 809,500 0,500" fill="url(#redBand)"/>

      <!-- headline -->
      <g transform="skewX(-10)">
        <text class="headline" x="168" y="292" fill="url(#silverText)">SERVICE</text>
        <text class="headline" x="168" y="442" fill="url(#silverText)">PARTS</text>
      </g>

      <!-- warranty badge -->
      <g class="warranty-badge">
        <path d="M166,478 L220,496 L216,560 Q210,592 166,610 Q122,592 116,560 L112,496 Z" fill="#d8d8d8"/>
        <path d="M166,490 L208,504 L205,556 Q200,582 166,597 Q132,582 127,556 L124,504 Z" fill="var(--brand-red)"/>
        <text class="warranty-number" x="166" y="556" text-anchor="middle">6</text>
        <polygon points="214,520 340,520 352,548 214,548" fill="#9d0a10"/>
        <text class="warranty-label" x="236" y="540" fill="#ffffff">MONTH</text>
        <rect x="214" y="551" width="172" height="28" fill="#f2f2f2"/>
        <text class="warranty-label" x="236" y="571" fill="var(--ink-dark)">WARRANTY</text>
      </g>

      <!-- red dash strip -->
      <rect class="dash-strip" x="404" y="565" width="400" height="14" fill="url(#redDashes)"/>

      <!-- brand -->
      <text class="brand-name" x="877" y="112" text-anchor="middle">KEM</text>
      <text class="brand-tagline" x="877" y="136" text-anchor="middle">AUTOMOTIVE COMPONENTS</text>

      <!-- product image area -->
      <rect class="product-image" x="814" y="160" width="250" height="405" rx="6" fill="url(#productArea)" opacity="0.55" role="img" aria-label="Product photo: pair of stabiliser link rods with threaded ends and rubber bushings"/>
    </svg>
  </div>
</body>
</html>
```